Stationary for Crestline Counsel Guild

I need stationary for Crestline Counsel Guild which
uses our logo
uses our address at:

3182 Willow Tern Parkway
Suite 480
Las Vegas, Nevada 89147

uses our phone number:
(877)HALO942
(877)425-6942

Classy Design with Power and Integrity
I ALSO NEED A SECOND SHEET FOR LETTERS
AND
A 10" by 13" ENVELOPE
AS WELL AS REGULAR ENVELOPE

AND
A 10" by 13" ENVELOPE

uses our website:
www.CrestlineCounselGuild.example

uses our email address
info@CrestlineCounselGuild.example

AND

A 10" by 13" ENVELOPE

                                   

                               

AND

A 10" by 13" ENVELOPE

                                   

Please make sure that you have used the latest updated logo supplied in brief on this project.  Also please make sure that the logo AND the words CRESTLINE COUNSEL GUILD is prominent on th etop of letterhead.  I look forwrad to your editions.  Marlon Tavish President

Update: Please use the updated logo on the letterhead and envelopes.  I want the LOGO prominant and centered at the top of page with CRESTLINE COUNSEL GUILD (Use Traditional and powerful font similar to Georgian or like in power and tradition) under it with address, telephone, email and wedsite information.  I also want a second page for letter with similar look but no logo in top of page with info at bottom of second page.  I will make a decide on design quickly.  Thank you vesy much.

Reason: Update: Please use the updated logo on the letterhead and envelopes. I want the LOGO prominant and centered at the top of page with CRESTLINE COUNSEL GUILD (Use Traditional and powerful font similar to Georgian or like in power and tradition) under it with address, telephone, email and wedsite information. I also want a second page for letter with similar look but no logo in top of page with info at bottom of second page. I will make a decide on design quickly. Thank you vesy much.

Target Market(s)

Attorneys invited to join organization.

Requirements
Must have
• Classy Design with Power and Integrity
AND
A 10" by 13" ENVELOPE

Update: Please use the updated logo on the letterhead and envelopes. I want the LOGO prominant and centered at the top of page with CRESTLINE COUNSEL GUILD (Use Traditional and powerful font similar to Georgian or like in power and tradition) under it with address, telephone, email and wedsite information. I also want a second page for letter with similar look but no logo in top of page with info at bottom of second page. I will make a decide on design quickly. Thank you vesy much.
Nice to have
AND
A 10" by 13" ENVELOPE
Should not have
• Nothing casual or funny

```html
<!DOCTYPE html>
<html lang="en">
<head>
<meta charset="utf-8">
<title>Crestline Counsel Guild — Stationery</title>
<link rel="stylesheet" href="https://fonts.googleapis.com/css2?family=Cinzel:wght@700&family=Crimson+Pro:wght@400;500&display=swap">
<style>
  :root {
    --stage: #000000;
    --paper: #ffffff;
    --ink: #111111;
    --muted: #6b6b6b;
    --seal: #8b1a1c;
    --band: #231f20;
    --band-text: #ffffff;
    --rule: #555555;
  }
  * { margin: 0; padding: 0; box-sizing: border-box; }
  html, body { width: 1200px; height: 1200px; overflow: hidden; background: var(--stage); }
  .stage { position: relative; width: 1200px; height: 1200px; }

  .brand-name {
    font-family: "Cinzel", "Times New Roman", serif;
    font-weight: 700;
    color: var(--ink);
    letter-spacing: 0.02em;
    white-space: nowrap;
  }
  .seal { position: absolute; display: block; }

  .letterhead {
    position: absolute; left: 207px; top: 45px; width: 786px; height: 1108px;
    background: var(--paper);
  }
  .letterhead .seal { left: 345px; top: 25px; }
  .letterhead .brand-name {
    position: absolute; left: 0; right: 0; top: 181px; text-align: center; font-size: 20px;
  }
  .letterhead-footer {
    position: absolute; left: 210px; width: 364px; top: 1037px;
    border-top: 1px solid var(--rule);
    padding-top: 7px;
    text-align: center;
    font-family: "Crimson Pro", "Times New Roman", serif;
    font-weight: 500;
    font-size: 10.5px; line-height: 13px; color: var(--ink);
  }

  .envelope {
    position: absolute; left: 159px; top: 513px; width: 880px; height: 440px;
    background: var(--paper);
    box-shadow: 0 2px 8px rgba(0,0,0,0.35);
  }
  .envelope .seal { left: 134px; top: 27px; }
  .envelope .return-address {
    position: absolute; left: 0; width: 368px; top: 140px; text-align: center;
  }
  .envelope .brand-name { font-size: 19px; }
  .envelope address {
    font-style: normal;
    font-family: "Crimson Pro", "Times New Roman", serif;
    font-weight: 500;
    font-size: 11px; line-height: 13px; color: var(--ink); margin-top: 4px;
  }

  .business-card {
    position: absolute; left: 522px; top: 419px; width: 444px; height: 273px;
    background: var(--paper);
    box-shadow: 0 3px 10px rgba(0,0,0,0.4);
  }
  .business-card .seal { left: 191px; top: 15px; }
  .business-card .brand-name {
    position: absolute; left: 0; right: 0; top: 86px; text-align: center;
    font-size: 15px; font-weight: 700;
  }
  .card-holder {
    position: absolute; left: 0; right: 0; top: 126px; text-align: center;
    font-family: "Crimson Pro", "Times New Roman", serif;
  }
  .card-holder .holder-name { font-size: 19px; color: var(--ink); line-height: 22px; }
  .card-holder .holder-title { font-size: 13px; color: var(--muted); line-height: 16px; }
  .card-contact {
    position: absolute; left: 0; right: 0; bottom: 0; height: 62px;
    background: var(--band); color: var(--band-text);
    text-align: center;
    font-family: "Crimson Pro", "Times New Roman", serif;
    font-size: 12px; line-height: 15.5px; padding-top: 7px;
  }
</style>
</head>
<body>
<main class="stage">

  <section class="letterhead" aria-label="Letterhead">
    <svg class="seal" width="96" height="96" viewBox="0 0 96 96" aria-hidden="true"><circle cx="48" cy="48" r="46" fill="var(--seal)"/></svg>
    <h1 class="brand-name">CRESTLINE COUNSEL GUILD</h1>
    <footer class="letterhead-footer">
      <p>3182 Willow Tern Parkway | Suite 480 | Las Vegas, Nevada 89147</p>
      <p>T. (877)HALO942 | T. (877)425-6942</p>
      <p>www.CrestlineCounselGuild.example</p>
    </footer>
  </section>

  <section class="envelope" aria-label="Envelope">
    <svg class="seal" width="100" height="100" viewBox="0 0 100 100" aria-hidden="true"><circle cx="50" cy="50" r="48" fill="var(--seal)"/></svg>
    <div class="return-address">
      <p class="brand-name">CRESTLINE COUNSEL GUILD</p>
      <address>3182 Willow Tern Parkway, Suite 480<br>Las Vegas, Nevada 89147</address>
    </div>
  </section>

  <section class="business-card" aria-label="Business card">
    <svg class="seal" width="62" height="62" viewBox="0 0 62 62" aria-hidden="true"><circle cx="31" cy="31" r="30" fill="var(--seal)"/></svg>
    <p class="brand-name">CRESTLINE COUNSEL GUILD</p>
    <div class="card-holder">
      <p class="holder-name">Dorian Vale</p>
      <p class="holder-title">Attorney</p>
    </div>
    <div class="card-contact">
      <p>3182 Willow Tern Parkway, Suite 480, Las Vegas, Nevada 89147</p>
      <p>Phone : (877)HALO942, Fax : (877)425-6942</p>
      <p>www.CrestlineCounselGuild.example</p>
    </div>
  </section>

</main>
</body>
</html>
```